Wander Pose Journeys Postcard Design

We need a promotional CMYK postcard that we will leave at yoga studios to advertise our yoga holidays to Cambodia.

Filecrate link with possible photos + logos (please see photo notes below): https://www.filecrate.net/sh/4kqpw81xz3m5v9a/BBLmtyyq0K3Pz7RVbnGhQeLu?dl=0

Please message me if you need more info or have issues with the photos.

Thanks

Target Market(s)

Brand style:
High quality and discerning, healthy and ethically aware, natural, unique and boutique, a sense of exploration, pitched at busy professionals and high end consumers. (not hippy!)

Industry/Entity Type

Travel

Font styles to use
Serif
Sans Serif

Colors
abd036
0492cd

Requirements
Must have
• CMYK
• *I have attached a file crate link to various named pictures that you may use for your design selection but you are free to supply other royalty free pictures if you wish. There are a number of choices and we do not expect all of these to be used - just offering a selection so hopefully some will be suitable for your design. Here is the filecrate link: https://www.filecrate.net/sh/4kqpw81xz3m5v9a/BBLmtyyq0K3Pz7RVbnGhQeLu?dl=0
• *Main front Picture must be one associated with Cambodia. Expecting several smaller photos on front as well
• *Must have at least one of our yoga photos on it.
• *The reverse side must have some white space around the address area so people could write a few lines and send as a postcard.
• *Please use the logo colours (lime and turquoise) with black or white as the main theme/colours.
• *Thinking to have a main photo of Cambodia on front with smaller photos and the 7 words featured (see text below).
• Text to include
• Front of postcard:
• (WPJ logo - prefer the coloured logo but needs to look ok with rest of photo - so can have white or black background or I have it in black & white - have attached coloured but message me if you wish for all B&W logo)
• Wander Pose Journeys
• Wander, never settle!
• 7 night Grand Asana Getaway Bundle.
• Siem Reap, Cambodia
• Discover
• Relax
• Cuisine
• Culture
• Yoga
• Boutique
• Ethical travel
• Reverse of postcard:
• Boutique, Unique, Fantastique!
• Do you need a high quality cultural holiday that explores, experiences, delights, relaxes, indulges - and has daily yoga? Are you short of time to do your holiday planning but still want some choices. Do you prefer a holiday over a strict yoga retreat? Do you want to use an ethical travel company to ensure your vacation does some good for others as well?
• Then visit:
• wanderposejourneys.com
• for dates and details.
• (also needs a box that I can stamp different codes into - must have white background - stamp text height is 4mm and max width is 27mm - needs the following text in or around the box)
• Special Promotion Code:
• Use this code with booking to receive a $200 AUD Movaleta ecard
Nice to have
• Printers Specification (please see Printlane.com.au for other specifications if needed)
• Acceptable File Formats:
• We support a variety of file formats for uploaded designs.
• Adobe Acrobat 9 Document (*.pdf) (recommended)
• JPEG Image (*.jpg,*.jpeg)
• A6 postcard size:
• Full Bleed Size
• 151 x 108 mm
• 1783 x 1275 pixels
• Document Trim Size
• 148 x 105 mm
• 1748 x 1240 pixels
• CMYK
• Digital Imaging
• You may create printed products on our web site using digitized images from a variety of sources. Your designs, photos and images can come from a digital camera, scanner, or the Web.
• Any image you plan to use must be saved at approximately 300-dpi at 100% output size for the very best printing results. It’s helpful to know that shrinking an image on a product will increase its resolution. For example, an image captured at 600 x 900 pixels has 150-dpi at 4” x 6”. Howver, it can be printed at 300-dpi by reducing its dimensions on the product to 2” x 3”.
• Images from a Digital Camera
• If you wish to use images from a digital camera, before you snap pictures make sure the camera is set at a high enough resolution to result in 300 DPI at the intended photo print size. Most cameras have various settings for resolutions. The highest resolution for your camera depends on how many megapixels it has.
• You cannot increase the resolution of a photo after it is taken, except by reducing its printed dimensions (after you upload the image). Be careful when cropping a photo after it is taken. Cropping will reduce the number of pixels in the final image.
• Images from a Scanner
• Like a digital camera, a scanner must be preset to the proper resolution before image capture. Many scanners default to 150-dpi (or spi). Set your scanner’s resolution so that it results in 300-dpi at the image’s final print size. If your resulting scanned image is smaller than the recommended size or has less dpi than you need, you should either rescan your original at a higher resolution, or use the image for a smaller printed area.
• Images from the Web
• Images found on the web are typically at a resolution of 72-dpi. This resolution is much too low for quality printing. In addition, most images on the web are protected by copyright laws. For these reasons, we do not recommend using images from the web.
Should not have
• Hippy elements

```html
<!DOCTYPE html>
<html lang="en">
<head>
<meta charset="utf-8">
<title>Wander Pose Journeys – Postcard Reverse</title>
<link href="https://fonts.googleapis.com/css2?family=Roboto+Condensed:wght@300;700&family=Chewy&family=Patrick+Hand&display=swap" rel="stylesheet">
<style>
  :root {
    --navy: #0b2060;
    --white: #ffffff;
    --sky: #3cb4ee;
    --lime: #a8d832;
    --ink: #1a1a1a;
    --photo-sky: #bcd8ee;
    --photo-leaf: #5e8f2e;
    --photo-stone: #7d7a52;
  }
  html, body {
    margin: 0;
    padding: 0;
    width: 1200px;
    height: 864px;
    overflow: hidden;
    background: var(--white);
  }
  .postcard {
    position: relative;
    width: 1200px;
    height: 864px;
    background: var(--white);
  }
  .message-panel {
    position: absolute;
    left: 0;
    top: 0;
    width: 638px;
    height: 600px;
    background: var(--navy);
    color: var(--white);
    font-family: "Roboto Condensed", "Arial Narrow", sans-serif;
  }
  .headline {
    position: absolute;
    left: 0;
    width: 590px;
    top: 28px;
    margin: 0;
    text-align: center;
    font-weight: 700;
    font-size: 35px;
    letter-spacing: 0.2px;
  }
  .pitch {
    position: absolute;
    left: 38px;
    top: 92px;
    width: 562px;
    margin: 0;
    font-weight: 300;
    font-size: 26px;
    line-height: 33.8px;
    text-align: justify;
  }
  .visit-label {
    position: absolute;
    left: 0;
    width: 590px;
    top: 338px;
    margin: 0;
    text-align: center;
    font-weight: 300;
    font-size: 25px;
    color: var(--sky);
  }
  .website {
    position: absolute;
    left: 0;
    width: 590px;
    top: 372px;
    margin: 0;
    text-align: center;
    font-weight: 300;
    font-size: 34px;
    color: var(--lime);
  }
  .field {
    position: absolute;
    margin: 0;
    font-weight: 300;
    font-size: 25px;
  }
  .field-dates { left: 118px; top: 426px; }
  .field-code { left: 102px; top: 471px; }
  .code-box {
    position: absolute;
    background: var(--white);
    border-radius: 6px;
  }
  .code-box-dates { left: 320px; top: 430px; width: 139px; height: 25px; }
  .code-box-promo { left: 359px; top: 476px; width: 100px; height: 25px; }
  .offer {
    position: absolute;
    left: 0;
    width: 638px;
    top: 506px;
    margin: 0;
    text-align: center;
    font-family: "Chewy", "Comic Sans MS", cursive;
    font-size: 33px;
    line-height: 46px;
    letter-spacing: 0.8px;
    color: var(--lime);
  }
  .temple-photo {
    position: absolute;
    left: 0;
    top: 600px;
    width: 638px;
    height: 264px;
    background:
      linear-gradient(180deg, var(--photo-sky) 0%, rgba(188,216,238,0) 35%),
      linear-gradient(90deg, var(--photo-leaf) 0%, var(--photo-stone) 45%, #a69a86 62%, var(--photo-leaf) 100%);
  }
  .stamp-box {
    position: absolute;
    left: 998px;
    top: 57px;
    width: 148px;
    height: 125px;
  }
  .stamp-label {
    position: absolute;
    left: 998px;
    top: 94px;
    width: 150px;
    margin: 0;
    text-align: center;
    font-family: "Patrick Hand", "Comic Sans MS", cursive;
    font-size: 19px;
    line-height: 26px;
    color: var(--ink);
  }
</style>
</head>
<body>
<main class="postcard">
  <section class="message-panel">
    <h1 class="headline">Boutique, Unique, Fantastique!</h1>
    <p class="pitch">Do you need a high quality cultural holiday that explores, experiences, delights, relaxes, indulges - and has daily yoga? Are you short of time to do your holiday planning but still want some choices. Do you prefer a holiday over a strict yoga retreat? Do you want to use an ethical travel company to ensure your vacation does some good for others as well?</p>
    <p class="visit-label">Then visit:</p>
    <p class="website">wanderposejourneys.com</p>
    <p class="field field-dates">dates and details:</p>
    <div class="code-box code-box-dates"></div>
    <p class="field field-code">Special Promotion Code:</p>
    <div class="code-box code-box-promo"></div>
    <p class="offer">Use this code with booking to<br>receive a $200 AUD Movaleta ecard</p>
  </section>

  <div class="temple-photo" role="img" aria-label="Photo of a moss-covered Cambodian temple ruin with giant tree roots growing over the stone walls"></div>

  <svg class="stamp-box" width="148" height="125" viewBox="0 0 148 125" aria-hidden="true">
    <rect x="1.5" y="1.5" width="145" height="122" fill="none" stroke="#1a1a1a" stroke-width="3" stroke-dasharray="9 6"/>
  </svg>
  <p class="stamp-label">stamp<br>here</p>
</main>
</body>
</html>
```